Brook Lantern Stationery Design Project

We need complete stationary design for a start up company called "Brook Lantern". We develop B2B and B2C SAAS based solutions and e-commerce portals for companies. The design should communicate simplicity and elegance. The domain name of the site will be brooklantern.com. The logo of the company is https://files.vexipod.net/u/8147205/7730_2093318_41862_image.jpg
Updates

Target Market(s)

B2B and B2C

Industry/Entity Type

E-Commerce

Requirements
Must have
• The design should reflect the followings:
- Company logo
- Company activities
- Be modern
Nice to have
• Preferably, the colors of the logo are to be used, but we are open for suggestions.

A design with transparent background might be nice.

```html
<!DOCTYPE html>
<html lang="en">
<head>
<meta charset="utf-8">
<title>Brook Lantern — Business Cards</title>
<link rel="stylesheet" href="https://fonts.googleapis.com/css2?family=Open+Sans:wght@400;600;700&display=swap">
<style>
  :root {
    --page: #f3f3f4;
    --card-light: #ffffff;
    --card-dark: #232f5a;
    --brand-red: #d3293b;
    --brand-blue: #2a6fbd;
    --ink-grey: #6b6c70;
    --ink-light: #ffffff;
    --divider-light: #9a9ba0;
    --divider-dark: #ffffff;
  }
  * { box-sizing: border-box; margin: 0; padding: 0; }
  html, body {
    width: 1200px;
    height: 902px;
    overflow: hidden;
    background: var(--page);
    font-family: "Open Sans", Arial, sans-serif;
  }
  .sheet {
    width: 1200px;
    height: 902px;
    display: flex;
    align-items: center;
    justify-content: center;
    gap: 44px;
  }
  .card {
    width: 530px;
    height: 303px;
    display: flex;
    align-items: center;
    justify-content: center;
    box-shadow: 0 6px 18px rgba(0, 0, 0, 0.12);
  }
  .card--front { background: var(--card-light); color: var(--ink-grey); }
  .card--back  { background: var(--card-dark);  color: var(--ink-light); }

  .brand-block {
    display: flex;
    flex-direction: column;
    align-items: flex-end;
    padding-right: 22px;
  }
  .wordmark {
    display: flex;
    align-items: center;
    gap: 8px;
    margin-bottom: 12px;
  }
  .wordmark__dot {
    width: 14px;
    height: 14px;
    border-radius: 50%;
    background: var(--brand-blue);
  }
  .wordmark__name {
    font-size: 22px;
    font-weight: 700;
    color: var(--brand-red);
    letter-spacing: -0.2px;
  }
  .card--back .wordmark__name { color: var(--ink-light); }

  .tagline {
    font-size: 11.5px;
    font-weight: 700;
    line-height: 1.35;
    text-align: right;
  }

  .divider {
    width: 1.5px;
    height: 78px;
    background: var(--divider-light);
  }
  .card--back .divider { background: var(--divider-dark); }

  .contact-block {
    padding-left: 20px;
    font-size: 11.5px;
    line-height: 1.4;
  }
  .contact-block__name {
    font-size: 13.5px;
    font-weight: 700;
    margin-bottom: 4px;
  }
  .accent-rules {
    display: block;
    margin-bottom: 8px;
  }
  .contact-block__line { display: block; }
</style>
</head>
<body>
<main class="sheet">

  <section class="card card--front" aria-label="Business card front">
    <div class="brand-block">
      <div class="wordmark">
        <span class="wordmark__dot"></span>
        <span class="wordmark__name">Brook Lantern</span>
      </div>
      <p class="tagline">develop B2B and B2C SAAS based<br>solutions e-commerce portals<br>for companies</p>
    </div>
    <div class="divider"></div>
    <div class="contact-block">
      <p class="contact-block__name">Arjun Mehra</p>
      <svg class="accent-rules" width="66" height="10" viewBox="0 0 66 10" aria-hidden="true">
        <line x1="0" y1="2" x2="66" y2="2" stroke="var(--brand-red)" stroke-width="2.2"/>
        <line x1="0" y1="8" x2="66" y2="8" stroke="var(--brand-blue)" stroke-width="2.2"/>
      </svg>
      <span class="contact-block__line">+1-555 210 4836</span>
      <span class="contact-block__line">info@brooklantern.in</span>
      <span class="contact-block__line">www.brooklantern.com</span>
    </div>
  </section>

  <section class="card card--back" aria-label="Business card back">
    <div class="brand-block">
      <div class="wordmark">
        <span class="wordmark__dot"></span>
        <span class="wordmark__name">Brook Lantern</span>
      </div>
      <p class="tagline">develop B2B and B2C SAAS based<br>solutions e-commerce portals<br>for companies</p>
    </div>
    <div class="divider"></div>
    <div class="contact-block">
      <p class="contact-block__name">Arjun Mehra</p>
      <svg class="accent-rules" width="66" height="10" viewBox="0 0 66 10" aria-hidden="true">
        <line x1="0" y1="2" x2="66" y2="2" stroke="var(--brand-red)" stroke-width="2.2"/>
        <line x1="0" y1="8" x2="66" y2="8" stroke="var(--brand-blue)" stroke-width="2.2"/>
      </svg>
      <span class="contact-block__line">+1-555 210 4836</span>
      <span class="contact-block__line">info@brooklantern.in</span>
      <span class="contact-block__line">www.brooklantern.com</span>
    </div>
  </section>

</main>
</body>
</html>
```